A start up Private Wine Label for export to Asia.

We are looking for the best graphic design for our very first wine label Corvessa Cellars and would like the following requirements:

1. Black background - explore and play around the shade of black
2. Gold Shimmery Colour Font
3. Font should be a cursive classic posh that says Corvessa Cellars
4. We would like the front graphic design to be simple and elegant and has a traditional classic feel to it.

Target Market(s)

Small scale to test the upper class market for export to Asia

Font styles to use
Script

Colors

Designer to choose colors to be used in the design.

Requirements
Must have
• Gold font for the label Corvessa Cellars with shimmery touch to it.
• Elegant black background.
• Simple but elegant design.
• Attractive to the upper class market in Asia.
Nice to have
• Explore and play around with your imagination.

```html
<!DOCTYPE html>
<html lang="en">
<head>
<meta charset="utf-8">
<title>Corvessa Wine Label</title>
<link rel="stylesheet" href="https://fonts.googleapis.com/css2?family=Pinyon+Script&display=swap">
<style>
  :root {
    --backdrop: #eeeceb;
    --label-black: #050505;
    --gold-light: #fff1a8;
    --gold-mid: #e2b227;
    --gold-deep: #a8761a;
    --rule-gold: rgba(214, 170, 60, 0.45);
  }
  html, body {
    margin: 0;
    width: 1200px;
    height: 1200px;
    overflow: hidden;
    background: var(--backdrop);
  }
  .canvas {
    position: relative;
    width: 1200px;
    height: 1200px;
  }
  .wine-label {
    position: absolute;
    left: 360px;
    top: 108px;
    width: 480px;
    height: 984px;
    filter: drop-shadow(0 14px 22px rgba(0,0,0,0.22));
  }
  .label-art {
    position: absolute;
    inset: 0;
  }
  .brand-name {
    position: absolute;
    left: 0;
    right: 0;
    margin: 0;
    text-align: center;
    white-space: nowrap;
    font-family: "Pinyon Script", cursive;
    font-weight: 400;
    font-size: 100px;
    line-height: 1.2;
    background: linear-gradient(180deg, var(--gold-light) 0%, var(--gold-mid) 48%, var(--gold-deep) 100%);
    -webkit-background-clip: text;
    background-clip: text;
    color: transparent;
  }
  .brand-name--house { top: 372px; }
  .brand-name--wine  { top: 470px; }
</style>
</head>
<body>
<main class="canvas">
  <section class="wine-label">
    <svg class="label-art" viewBox="0 0 480 984" width="480" height="984">
      <defs>
        <linearGradient id="goldFrame" x1="0" y1="0" x2="1" y2="1">
          <stop offset="0" stop-color="#f7d55a"/>
          <stop offset="0.35" stop-color="#fff0a0"/>
          <stop offset="0.6" stop-color="#d9a526"/>
          <stop offset="1" stop-color="#f2cf55"/>
        </linearGradient>
        <linearGradient id="goldBand" x1="0" y1="0" x2="0" y2="1">
          <stop offset="0" stop-color="#b8861c"/>
          <stop offset="0.3" stop-color="#fbe27a"/>
          <stop offset="0.7" stop-color="#e8b92f"/>
          <stop offset="1" stop-color="#a87418"/>
        </linearGradient>
        <linearGradient id="gloss" x1="0" y1="0" x2="1" y2="1">
          <stop offset="0" stop-color="#3a3a3a" stop-opacity="0.55"/>
          <stop offset="1" stop-color="#1a1a1a" stop-opacity="0.1"/>
        </linearGradient>
        <radialGradient id="sealRed" cx="0.55" cy="0.55" r="0.6">
          <stop offset="0" stop-color="#f06a2a"/>
          <stop offset="0.5" stop-color="#c0261a"/>
          <stop offset="1" stop-color="#7a0e0c"/>
        </radialGradient>
      </defs>

      <path class="frame-outer" fill="url(#goldFrame)"
        d="M44,0 H436 A44,44 0 0 0 480,44 V940 A44,44 0 0 0 436,984 H44 A44,44 0 0 0 0,940 V44 A44,44 0 0 0 44,0 Z"/>
      <path class="frame-inner-line" fill="none" stroke="#8a5e12" stroke-width="2"
        d="M50,10 H430 A40,40 0 0 0 470,50 V934 A40,40 0 0 0 430,974 H50 A40,40 0 0 0 10,934 V50 A40,40 0 0 0 50,10 Z"/>

      <path class="label-panel" fill="var(--label-black)"
        d="M56,22 H424 A34,34 0 0 0 458,56 V928 A34,34 0 0 0 424,962 H56 A34,34 0 0 0 22,928 V56 A34,34 0 0 0 56,22 Z"/>
      <path class="panel-gloss" fill="url(#gloss)"
        d="M56,22 H424 A34,34 0 0 0 458,56 V150 L22,610 V56 A34,34 0 0 0 56,22 Z"/>

      <line class="name-rule" x1="44" y1="370" x2="436" y2="370" stroke="var(--rule-gold)" stroke-width="1.5"/>
      <line class="name-rule" x1="44" y1="600" x2="436" y2="600" stroke="var(--rule-gold)" stroke-width="1.5"/>

      <rect class="gold-band" x="22" y="700" width="436" height="92" fill="url(#goldBand)"/>

      <circle class="wax-seal" cx="240" cy="746" r="78" fill="url(#sealRed)"
        role="img" aria-label="Red wax seal"/>
    </svg>

    <p class="brand-name brand-name--house">Corvessa</p>
    <p class="brand-name brand-name--wine">Wine</p>
  </section>
</main>
</body>
</html>
```